Packaging design for a Deli Shop "TORVO Gourmet"

We need a packaging design for a new Deli Business we are opening soon. We produce food to be packaged and sold either fresh or frozen in transparent disposable plastic boxes, cardboard boxes and finally delivered in a bag (Paper, plastic or shopping bag whatever goes best with the design) to take out. The food we generally pack are salads, lasagnas, ceviches, sandwiches, cookies, granola, dips, etc.

The name of the company is "TORVO Gourmet" Check our website for reference: www.torvogourmet-example.com

We have a logo and a name we want to maintain (attached).

The product will be sold in our new deli store, that is inspired in big cities delikatessen, quite modern and trendy. It also delivers a message that everything we sell is high quality, artisan (not massive or mainstream) and great in flavors.

Packaging must communicate freshness, great flavor, high quality and high price.

Packaging must be feasible to produce and print easily without any complex or impossible to implement packaging, (preferrable to be done or easy to adapt from generic packaging).

All our communication will be in Spanish so please do not depend on english for the design. If english or any other language is used, please be sure its understandable in almost any country (ie Basic English, Italian).

Same packaging (labeling or boxes and bags) will be used, just changing the name of the product inside according to the product.

Most of our product will be displayed in refrigerators and freezers.
Updates

I just uploaded a visual brief of the packaging examples we would like to have.

Looking forward to see your designs.
Thank you

Project Deadline Extended
Reason: Some designers who said will participate havent submitted their deaigns, and still what is being submitted is not fully complying with the requirements. Thank you

Target Market(s)

The main target is High SEL, between 24 and 40, mostly woman

Industry/Entity Type

Communication

Requirements
Must have

Nice to have
• Please take a look at my website www.torvogourmet-example.com to see the kind of coloring we are aiming to have.

Give the impression of being "Green"...

Include "Kraft" color paper / Brown paper color
Should not have
• Complex packaging difficult to implement in a simple print shop.
Expensive items.

```html
<!DOCTYPE html>
<html lang="es">
<head>
<meta charset="utf-8">
<title>TORVO Gourmet – Etiquetas</title>
<link rel="stylesheet" href="https://fonts.googleapis.com/css2?family=Rosarivo&display=swap">
<style>
  :root{
    --bg:#f4f1ea;
    --white:#ffffff;
    --brand-red:#c8372d;
    --green:#8cc63f;
    --green-dark:#6fa52b;
    --orange:#f2a31b;
    --orange-dark:#e08a10;
    --red:#c0262d;
    --red-dark:#a01d23;
    --name-green:#79b42e;
    --name-orange:#ee8f17;
    --fine:#a9a9a9;
  }
  *{box-sizing:border-box;margin:0;padding:0}
  html,body{width:1200px;height:616px;overflow:hidden;background:var(--bg)}
  body{font-family:"Rosarivo",Georgia,serif}
  .labels{display:flex;gap:60px;padding:73px 60px}
  .label{width:320px;height:470px;padding:10px;border-radius:4px;display:flex;flex-direction:column;
    box-shadow:0 6px 18px rgba(0,0,0,.12)}
  .label--spinach{--panel:var(--green);--panel-dark:var(--green-dark)}
  .label--greek{--panel:var(--orange);--panel-dark:var(--orange-dark)}
  .label--risotto{--panel:var(--red);--panel-dark:var(--red-dark)}
  .label{background:var(--panel)}
  .label__brand{background:var(--white);height:120px;display:flex;align-items:center;justify-content:center;gap:10px}
  .brand-mark{width:14px;height:14px;background:var(--brand-red)}
  .brand-name{color:var(--brand-red);font-size:30px;letter-spacing:1px}
  .label__body{flex:1;position:relative;display:flex;align-items:center;justify-content:center;
    background:radial-gradient(circle at 50% 50%,var(--panel) 0%,var(--panel-dark) 100%)}
  .label__pattern{position:absolute;inset:0}
  .name-card{position:relative;width:250px;height:170px;background:var(--white);border-radius:14px;
    display:flex;flex-direction:column;align-items:center;justify-content:center;text-align:center;padding:12px}
  .name-card__kind{color:var(--name-green);font-size:26px;line-height:1.1}
  .name-card__dish{color:var(--name-orange);font-size:38px;line-height:1.15;letter-spacing:1px}
  .name-card__note{color:var(--fine);font-size:10px;margin-top:12px;line-height:1.4}
</style>
</head>
<body>
<main class="labels">
  <article class="label label--spinach">
    <header class="label__brand"><span class="brand-mark"></span><span class="brand-name">TORVO Gourmet</span></header>
    <section class="label__body">
      <div class="label__pattern" role="img" aria-label="Patrón de hojas en tonos verdes"></div>
      <div class="name-card">
        <p class="name-card__kind">Ensalada de</p>
        <p class="name-card__dish">ESPINACA</p>
        <p class="name-card__note">Cocina artesanal<br>Consumir fresco</p>
      </div>
    </section>
  </article>

  <article class="label label--greek">
    <header class="label__brand"><span class="brand-mark"></span><span class="brand-name">TORVO Gourmet</span></header>
    <section class="label__body">
      <div class="label__pattern" role="img" aria-label="Patrón de hojas en tonos naranjas"></div>
      <div class="name-card">
        <p class="name-card__kind">Ensalada</p>
        <p class="name-card__dish">GRIEGA</p>
        <p class="name-card__note">Cocina artesanal<br>Consumir fresco</p>
      </div>
    </section>
  </article>

  <article class="label label--risotto">
    <header class="label__brand"><span class="brand-mark"></span><span class="brand-name">TORVO Gourmet</span></header>
    <section class="label__body">
      <div class="label__pattern" role="img" aria-label="Patrón de hojas en tonos rojos"></div>
      <div class="name-card">
        <p class="name-card__kind">Rissoto de</p>
        <p class="name-card__dish">FUNHI</p>
        <p class="name-card__note">Cocina artesanal<br>Consumir fresco</p>
      </div>
    </section>
  </article>
</main>
</body>
</html>
```